Web design required

1-We need a web design for existing company based in New Zealand
2-We build residential house and light commercial
3-We has in-house designer which allow us can provide interior design
4-We modeling project before site construction, which enable both client and construction team to visually analysis whole project,

Target Market(s)

middle class residential house market
Ref: http://www.brambleworthbuilders.co.nz/

Industry/Entity Type

Construction Company

Number of Pages Required

1 page

Font styles to use
Sans Serif
Other font styles liked:
• Such as : Central Gothic or similar which has more design taste

Colors

Designer to choose colors to be used in the design.

Requirements
Must have
• Front sheet, contact information, sample project

```html
<!DOCTYPE html>
<html lang="en">
<head>
<meta charset="utf-8">
<title>Kestrel Homes</title>
<link href="https://fonts.googleapis.com/css2?family=Questrial&family=Montserrat:wght@500;600;700&display=swap" rel="stylesheet">
<style>
:root{
  --blue:#0b5fa5;
  --blue-dark:#094d86;
  --ink:#1f1f1f;
  --muted:#8a8a8a;
  --light:#f0f0f0;
  --footer:#333333;
  --footer-text:#d8d8d8;
  --white:#ffffff;
}
*{margin:0;padding:0;box-sizing:border-box}
html,body{width:1200px;height:2830px;overflow:hidden;background:var(--white)}
body{position:relative;font-family:"Questrial",sans-serif;color:var(--ink)}
.abs{position:absolute}
.heading{font-family:"Montserrat",sans-serif;font-weight:600;font-size:26px;letter-spacing:.5px;color:var(--ink)}
.rule{width:66px;height:3px;background:var(--blue)}
.sub{font-size:14px;color:var(--blue)}
.btn{position:absolute;background:var(--blue);color:var(--white);border-radius:22px;display:flex;align-items:center;justify-content:center;font-family:"Montserrat",sans-serif;font-weight:600;font-size:13px;letter-spacing:.5px;text-transform:uppercase;white-space:nowrap}
.photo{position:absolute}

/* header */
.site-header{left:0;top:0;width:1200px;height:75px;background:var(--white)}
.brand{left:200px;top:20px;display:flex;align-items:center;gap:10px;font-family:"Montserrat",sans-serif;font-weight:700;font-size:24px;color:var(--ink)}
.brand-mark{width:34px;height:34px;background:var(--blue)}
.nav{left:0;top:31px;width:1200px;height:30px}
.nav a{position:absolute;font-size:11px;color:var(--ink);text-decoration:none;text-transform:uppercase;white-space:nowrap}
.nav a.active::after{content:"";position:absolute;left:2px;right:2px;top:19px;height:3px;background:var(--blue)}

/* hero */
.hero{left:0;top:75px;width:1200px;height:478px;background:linear-gradient(100deg,#3c4650 0%,#56616a 40%,#8d8f8f 60%,#c9c7c2 80%,#a8a6a2 100%)}
.hero-shade{left:0;top:75px;width:1200px;height:478px;background:rgba(20,25,30,.25)}
.hero-title{left:0;top:195px;width:1200px;text-align:center;color:var(--white);font-size:66px;line-height:74px;font-family:"Questrial",sans-serif;font-weight:400}
.counter{top:296px;color:var(--white);font-size:20px;padding-left:8px;border-left:2px solid var(--white);line-height:22px}
.hero-line{top:401px;height:2px;width:100px;background:var(--white)}

/* services */
.services{left:0;top:553px;width:1200px;height:749px;background:linear-gradient(135deg,#f4f4f4 0%,#e9e9e9 50%,#f3f3f3 100%)}
.tile-text{position:absolute;width:200px;height:160px;background:var(--white);padding:20px 24px}
.tile-text h3{font-family:"Montserrat",sans-serif;font-weight:600;font-size:14px;line-height:20px;text-transform:uppercase;color:var(--ink)}
.tile-text p{font-size:11.5px;line-height:18px;color:var(--muted);margin-top:8px}
.tile-text .btn{position:static;display:inline-flex;width:88px;height:26px;font-size:10px;margin-top:10px}

/* about */
.about-text p.body{font-size:12.5px;line-height:24px;color:var(--muted)}

/* projects */
.projects{left:0;top:1840px;width:1200px;height:590px;background:linear-gradient(135deg,#f2f2f2 0%,#e8e8e8 55%,#f1f1f1 100%)}
.project-label{position:absolute;height:45px;width:222px;background:var(--blue);color:var(--white);font-family:"Montserrat",sans-serif;font-weight:600;font-size:11.5px;display:flex;align-items:center;padding-left:16px;text-transform:uppercase;white-space:nowrap;overflow:hidden}

/* footer */
.footer{left:0;top:2430px;width:1200px;height:400px;background:var(--footer)}
.f-title{font-family:"Montserrat",sans-serif;font-weight:600;font-size:17px;color:var(--white);text-transform:uppercase}
.f-title .accent{color:var(--blue)}
.f-rule{width:40px;height:2px;background:var(--blue)}
.f-text{font-size:12px;line-height:24px;color:var(--footer-text)}
.social{position:absolute;width:28px;height:28px;border-radius:50%;background:var(--blue)}
.field{position:absolute;border:1px solid #cfcfcf;border-radius:20px;color:var(--footer-text);font-size:11px;padding:0 24px;display:flex;align-items:center}
.footer-bar{left:0;top:2789px;width:1200px;height:1px;background:#4a4a4a}
.legal{top:2805px;font-size:11.5px;color:var(--footer-text)}
</style>
</head>
<body>

<!-- header -->
<header class="site-header abs">
  <div class="brand abs"><span class="brand-mark"></span>KESTREL HOMES</div>
  <nav class="nav abs">
    <a class="active" style="left:523px">Home</a>
    <a style="left:598px">Services</a>
    <a style="left:696px">About us</a>
    <a style="left:793px">Projects</a>
    <a style="left:902px">Contact</a>
  </nav>
  <svg class="abs" style="left:982px;top:29px" width="16" height="16" viewBox="0 0 18 18" aria-label="Search"><circle cx="7.5" cy="7.5" r="5.5" fill="none" stroke="#1f1f1f" stroke-width="2"/><line x1="11.5" y1="11.5" x2="16" y2="16" stroke="#1f1f1f" stroke-width="2.2"/></svg>
</header>

<!-- hero -->
<section>
  <div class="hero abs" role="img" aria-label="Modern two-storey family home at dusk blending into a bright living room interior"></div>
  <div class="hero-shade abs"></div>
  <h1 class="hero-title abs">Welcome To Kestrel<br>Homes</h1>
  <div class="counter abs" style="left:90px">02</div>
  <div class="counter abs" style="left:1070px;border-left:none;border-right:2px solid #fff;padding:0 8px 0 0">04</div>
  <div class="hero-line abs" style="left:396px"></div>
  <a class="btn" style="left:528px;top:380px;width:144px;height:44px">Read more</a>
  <div class="hero-line abs" style="left:702px"></div>
</section>

<!-- services -->
<section class="services abs"></section>
<div class="rule abs" style="left:200px;top:636px"></div>
<h2 class="heading abs" style="left:200px;top:648px">OUR SERVICES</h2>
<p class="sub abs" style="left:200px;top:689px">Kestrel Homes works with you to take dream houses</p>

<div class="photo" style="left:200px;top:755px;width:400px;height:320px;background:linear-gradient(180deg,#3d5a85 0%,#7f90a8 45%,#cfcfcf 75%,#6b5a4a 100%)" role="img" aria-label="White weatherboard home lit up at twilight"></div>
<div class="tile-text" style="left:600px;top:755px">
  <h3>Preconstruction<br>planning</h3>
  <p>Lorem Ipsum is simply dummy text of printing</p>
  <a class="btn">Read more</a>
</div>
<div class="photo" style="left:800px;top:755px;width:198px;height:160px;background:linear-gradient(135deg,#f2f2f2,#cfcfcf)" role="img" aria-label="Architectural sketch of a house"></div>
<div class="photo" style="left:600px;top:915px;width:200px;height:160px;background:linear-gradient(135deg,#d9d3cc,#9a8f86)" role="img" aria-label="Hands reviewing building plans"></div>
<div class="tile-text" style="left:800px;top:915px;width:198px">
  <h3>Construction<br>modelling</h3>
  <p>Lorem Ipsum is simply dummy text ofprinting</p>
  <a class="btn">Read more</a>
</div>
<div class="photo" style="left:200px;top:1075px;width:200px;height:161px;background:linear-gradient(135deg,#8a8a84,#5a5650)" role="img" aria-label="Builders in hard hats reviewing plans on site"></div>
<div class="tile-text" style="left:400px;top:1075px;height:161px">
  <h3>Full project<br>management</h3>
  <p>Lorem Ipsum is simply dummy text of printing</p>
  <a class="btn">Read more</a>
</div>
<div class="photo" style="left:600px;top:1075px;width:398px;height:161px;background:linear-gradient(90deg,#a9a6a1,#d9d7d3 55%,#8e8b86)" role="img" aria-label="Modern living room with concrete fireplace"></div>

<!-- about -->
<section class="about-text">
  <div class="rule abs" style="left:200px;top:1416px"></div>
  <h2 class="heading abs" style="left:200px;top:1428px">ABOUT US</h2>
  <p class="sub abs" style="left:200px;top:1469px">Kestrel Homes works with you to take dream houses</p>
  <p class="body abs" style="left:200px;top:1508px;width:345px">Kestrel Homes is dedicated to creating and renovating beautiful and unusual buildings.Kestrel Homes works with you to take dream houses off the blueprints and into reality. We have the knowledge and expertise to customise homes to suit you – from unusual materials and designs to environmentally sensitive locations.</p>
  <a class="btn" style="left:200px;top:1706px;width:142px;height:42px">Read more</a>
</section>
<div class="photo" style="left:600px;top:1374px;width:342px;height:396px;background:linear-gradient(180deg,#3b4654 0%,#4d5560 50%,#7c7c7a 80%,#9a9894 100%)" role="img" aria-label="Dark clad modern home with garage"></div>
<div class="photo" style="left:942px;top:1304px;width:258px;height:532px;background:linear-gradient(180deg,#8a6a4c 0%,#ecebe7 8%,#cfd8c4 40%,#eeeeec 65%,#6d7480 100%)" role="img" aria-label="Bright lounge with large windows and white sofa"></div>

<!-- projects -->
<section class="projects abs"></section>
<div class="rule abs" style="left:200px;top:1918px"></div>
<h2 class="heading abs" style="left:200px;top:1930px">OUR PROJECTS</h2>

<div class="photo" style="left:200px;top:2004px;width:211px;height:211px;background:linear-gradient(135deg,#e6e4e1,#a0744e 50%,#efeeec)" role="img" aria-label="Interior with timber ceiling and staircase"></div>
<div class="project-label" style="left:217px;top:2204px">Rimu Bay Project - Interior</div>
<div class="photo" style="left:481px;top:2004px;width:211px;height:211px;background:linear-gradient(180deg,#3d5a85,#b9bcc2 55%,#6f6b66)" role="img" aria-label="White home at twilight"></div>
<div class="project-label" style="left:498px;top:2204px">Kowhai Rd Project</div>
<div class="photo" style="left:762px;top:2004px;width:211px;height:211px;background:linear-gradient(180deg,#c9c9c9,#3a3a3a 45%,#8a6a4c)" role="img" aria-label="Modern home with dark cladding and timber deck"></div>
<div class="project-label" style="left:779px;top:2204px">Rimu Bay Project</div>

<a class="btn" style="left:528px;top:2310px;width:144px;height:44px">View more</a>

<!-- footer -->
<footer class="footer abs"></footer>
<div class="f-rule abs" style="left:200px;top:2492px"></div>
<div class="f-title abs" style="left:200px;top:2507px;font-size:19px"><span class="accent">KESTREL</span> HOMES</div>
<p class="f-text abs" style="left:200px;top:2550px;width:210px">Kestrel Homes is dedicated to creating and renovating beautiful and unusual buildings.Kestrel Homes works with you to take dream houses off the blueprints</p>
<span class="social" style="left:200px;top:2694px"></span>
<span class="social" style="left:240px;top:2694px"></span>
<span class="social" style="left:280px;top:2694px"></span>
<span class="social" style="left:320px;top:2694px"></span>

<div class="f-rule abs" style="left:475px;top:2492px"></div>
<div class="f-title abs" style="left:475px;top:2510px;font-size:14px"><span class="accent">QUICK</span> LINKS</div>
<p class="f-text abs" style="left:475px;top:2550px">Home<br>Services<br>About<br>Projects<br>Contact</p>

<div class="f-rule abs" style="left:643px;top:2492px"></div>
<div class="f-title abs" style="left:643px;top:2510px;font-size:14px"><span class="accent">KEEP</span> IN TOUCH</div>
<div class="field" style="left:643px;top:2558px;width:172px;height:35px">Name :</div>
<div class="field" style="left:828px;top:2558px;width:170px;height:35px">Email :</div>
<div class="field" style="left:643px;top:2613px;width:355px;height:70px;align-items:flex-start;padding-top:12px">Message :</div>
<a class="btn" style="left:643px;top:2715px;width:108px;height:34px;font-size:11px">Read more</a>

<div class="footer-bar abs"></div>
<p class="legal abs" style="left:200px">© Copyright 2017 kestrelhomes.co.nz. All Rights Reserved.</p>
<p class="legal abs" style="left:913px">Privacy Policy</p>

</body>
</html>
```